Brochure Design Project

We are a Professional Employer Organization. We save employers time and money on workers' compensation, payroll and benefits.

```html
<!DOCTYPE html>
<html lang="en">
<head>
<meta charset="utf-8">
<title>Harbor Employee Management – Tri-fold Brochure</title>
<link rel="stylesheet" href="https://fonts.googleapis.com/css2?family=Roboto:wght@400;500;700&family=Roboto+Condensed:wght@700&display=swap">
<style>
:root{
  --stage:#4d4d4d;
  --gold:#e3a52a;
  --gold-deep:#d4931c;
  --gold-light:#f0bd4f;
  --ink:#1a1a1a;
  --white:#ffffff;
  --paper:#f4f4f4;
  --grey:#d9d9d9;
}
*{box-sizing:border-box;margin:0;padding:0}
html,body{width:1200px;height:1134px;overflow:hidden;background:var(--stage);font-family:"Roboto",Arial,sans-serif;color:var(--ink)}
.sheet{position:absolute;left:269px;width:658px;height:508px;overflow:hidden;box-shadow:0 3px 10px rgba(0,0,0,.45)}
.sheet--outside{top:50px}
.sheet--inside{top:582px;height:509px}
.panel{position:absolute;top:0;height:100%}
.panel--a{left:0;width:216px}
.panel--b{left:216px;width:218px;background:var(--gold)}
.panel--c{left:434px;width:224px}
.abs{position:absolute}

/* outside left */
.worry{background:linear-gradient(90deg,#fff 0%,#f3f3f3 60%,#d6d6d6 100%)}
.worry__title{left:11px;top:12px;font-size:9.6px;font-weight:700;line-height:12px;letter-spacing:.1px}
.worry__rule{left:11px;top:50px;width:165px;height:1.5px;background:var(--gold)}
.topic{position:absolute;left:10px;display:flex;align-items:center}
.topic__icon{width:17px;height:17px;border-radius:50%;background:var(--ink);display:flex;align-items:center;justify-content:center}
.topic__label{height:12px;margin-left:3px;padding:0 14px 0 4px;background:var(--gold);border-radius:0 7px 7px 0;color:#fff;font-size:7.6px;font-weight:700;line-height:12px;letter-spacing:.2px}
.list{position:absolute;left:14px;list-style:none;font-size:7px;line-height:11.5px}
.list li::before{content:"•";margin-right:5px;font-size:6px}

/* outside middle */
.mid-text{color:#fff;font-size:6.8px;line-height:9.8px}
.mid-text--justify{text-align:justify}
.mid-bullets{list-style:none;color:#fff;font-size:6.8px;line-height:11.5px;text-transform:uppercase}
.mid-bullets li::before{content:"♦";font-size:5px;margin-right:4px;vertical-align:1px}
.mid-rule{height:1px;background:rgba(255,255,255,.55)}
.brand{font-family:"Roboto Condensed","Arial Narrow",sans-serif;font-weight:700;letter-spacing:.5px}
.contact-row{display:flex;align-items:center;font-size:10.5px;color:#111}
.contact-row svg{margin-right:9px}

/* outside right */
.cover{background:var(--gold)}
.cover__card{left:17px;top:0;width:188px;height:336px;background:#fff;border-radius:0 0 94px 94px}
.cover__photo{left:23px;top:86px;width:176px;height:246px;border-radius:0 0 88px 88px;background:linear-gradient(180deg,#e8e2da 0%,#6c6a70 45%,#2a2a30 100%)}
.cover__name{left:17px;top:30px;width:188px;text-align:center;color:var(--gold);font-size:24px;line-height:26px}
.cover__sub{left:17px;top:69px;width:188px;text-align:center;font-size:5.6px;font-weight:700;letter-spacing:.2px}
.cover__head{left:0;width:224px;text-align:center;font-size:14px;font-weight:700;line-height:17px;color:var(--ink)}
.cover__note{left:0;top:442px;width:224px;text-align:center;font-size:8.2px;line-height:12px}
.call{left:8px;top:474px;width:202px;height:25px;border-radius:13px;background:var(--ink);color:#fff;display:flex;align-items:center;padding-left:18px}
.call__lead{font-size:13px;margin-right:10px}
.call__icon{width:22px;height:22px;border-radius:50%;background:#fff;display:flex;align-items:center;justify-content:center;margin-right:8px}
.call__num{font-size:14px;font-weight:700}

/* inside left */
.intro{background:#fff}
.intro__title{left:11px;top:15px;font-size:11.6px;font-weight:700;color:var(--gold);letter-spacing:.2px}
.intro__text{left:11px;width:196px;font-size:7px;line-height:9.8px;text-align:justify}

/* inside middle */
.care__title{left:10px;top:12px;width:200px;color:#fff;font-size:11.6px;font-weight:500;line-height:14px}
.care__rule{left:10px;top:42px;width:196px;height:1.5px;background:#fff}
.care__list{left:20px;top:55px;list-style:none;color:#fff;font-size:7.4px;line-height:14.7px}
.care__list li::before{content:"♦";font-size:5px;margin-right:5px;vertical-align:1px}
.consult{left:23px;top:385px;width:161px;height:108px;background:#fff;border:1.5px dashed var(--ink);border-radius:16px;text-align:center;padding-top:11px}
.consult__gold{color:var(--gold);font-weight:700;font-size:9.8px;line-height:12.5px}
.consult__dark{font-weight:700;font-size:10px;line-height:14px}
.consult__or{color:var(--gold);font-size:7px;line-height:12px}

/* inside right */
.closing{background:#fff}
.closing__text{left:7px;top:198px;width:210px;font-size:7px;line-height:9.8px;text-align:justify}
.closing__phone{left:12px;top:250px;font-size:17px;color:var(--gold);font-weight:400}
.closing__web{left:12px;top:272px;font-size:9.4px;color:#333}
</style>
</head>
<body>

<!-- Outside spread -->
<section class="sheet sheet--outside">

  <div class="panel panel--a worry">
    <h2 class="abs worry__title">WHEN YOU USE<br>HARBOR EMPLOYEE MANAGEMENT<br>YOU NO LONGER HAVE TO WORRY</h2>
    <div class="abs worry__rule"></div>

    <div class="topic" style="top:58px">
      <span class="topic__icon"><svg width="9" height="9" viewBox="0 0 10 10"><circle cx="5" cy="3.5" r="2" fill="#fff"/><rect x="1" y="6.5" width="8" height="2" rx="1" fill="#fff"/></svg></span>
      <span class="topic__label" style="width:130px">PAYROLL PROCESSING</span>
    </div>
    <ul class="list" style="top:79px">
      <li>the need for payroll software programs or updates</li>
      <li>payroll forms and supplies</li>
      <li>time spent on payroll processing</li>
      <li>garnishment &amp; child support administration</li>
      <li>direct deposits &amp; payroll related banking</li>
      <li>tax administration and deposits</li>
      <li>governmental payroll reporting</li>
      <li>W-2s and W-3s</li>
      <li>Employee regulatory compliance</li>
      <li>Wage verification</li>
    </ul>

    <div class="topic" style="top:204px">
      <span class="topic__icon"><svg width="9" height="9" viewBox="0 0 10 10"><circle cx="5" cy="4" r="3" fill="none" stroke="#fff" stroke-width="1.4"/><path d="M5 7v2.5" stroke="#fff" stroke-width="1.4"/></svg></span>
      <span class="topic__label" style="width:170px">HUMAN RESOURCE MANAGEMENT</span>
    </div>
    <ul class="list" style="top:226px">
      <li>new hire reporting &amp; state compliance</li>
      <li>employee files and record maintenance</li>
      <li>employee handbooks</li>
      <li>policy and procedures</li>
      <li>storage of employee records &amp; forms</li>
      <li>EEO reporting</li>
      <li>Employee &amp; regulatory compliance</li>
      <li>HR support</li>
    </ul>

    <div class="topic" style="top:331px">
      <span class="topic__icon"><svg width="9" height="9" viewBox="0 0 10 10"><circle cx="5" cy="3" r="2" fill="#fff"/><path d="M1 9.5c0-3 8-3 8 0z" fill="#fff"/></svg></span>
      <span class="topic__label" style="width:196px">WORKERS' COMPENSATION COVERAGE</span>
    </div>
    <ul class="list" style="top:354px">
      <li>the high prices of small business rates</li>
      <li>worksite safety programs &amp; training materials</li>
      <li>management of medical &amp; rehabilitation providers</li>
      <li>elimination of deposits and payroll audits</li>
      <li>fraud investigation</li>
    </ul>

    <div class="topic" style="top:423px">
      <span class="topic__icon"><svg width="9" height="9" viewBox="0 0 10 10"><circle cx="3" cy="3.5" r="1.6" fill="#fff"/><circle cx="7" cy="3.5" r="1.6" fill="#fff"/><path d="M0 9c0-3 10-3 10 0z" fill="#fff"/></svg></span>
      <span class="topic__label" style="width:118px">STATE UNEMPLOYMENT</span>
    </div>
    <ul class="list" style="top:445px">
      <li>Protect and dispute improper claims and charges</li>
      <li>Provide management information reports</li>
      <li>Audit state rate calculations</li>
      <li>Manage hearings and appeals</li>
    </ul>
  </div>

  <div class="panel panel--b">
    <p class="abs mid-text mid-text--justify" style="left:7px;top:38px;width:207px">By selecting Harbor Employee Management as your PEO you establish a co-employment relationship. HARBOR Employee Management takes on the administrative responsibility of managing your employees. Our all inclusive program includes the preparation and filing of payroll taxes and benefit administration, workers' compensation and federal and state unemployment. We work with you to ensure employee related governmental compliance, to easily manage your employer cost.</p>
    <p class="abs mid-text" style="left:7px;top:143px;font-size:7.8px;font-weight:500">Harbor Employee Management helps you to:</p>
    <ul class="abs mid-bullets" style="left:15px;top:161px">
      <li>Save time</li>
      <li>Reduce your employer payroll cost</li>
      <li>Simplify employee management</li>
      <li>Keep you in compliance with government</li>
      <li>Protect your business</li>
      <li>Offer competitive &amp; comprehensive benefit</li>
      <li>Programs</li>
    </ul>
    <div class="abs mid-rule" style="left:7px;top:262px;width:205px"></div>
    <p class="abs mid-text" style="left:7px;top:287px;width:207px">In short: You hire, fire, promote, direct and report who worked and how much. Harbor takes care of the rest so you can focus on growing your business</p>
    <div class="abs brand" style="left:0;top:383px;width:218px;text-align:center;color:#fff;font-size:25px">HARBOR</div>
    <div class="abs contact-row" style="left:43px;top:448px">
      <svg width="16" height="16" viewBox="0 0 16 16"><circle cx="8" cy="8" r="8" fill="#fff"/><path d="M5 4.2l1.6-.4.9 2.2-1 .8c.5 1.2 1.4 2.1 2.6 2.6l.8-1 2.2.9-.4 1.6c-3.4.3-7-3.3-6.7-6.7z" fill="#111"/></svg>
      800-555-0142
    </div>
    <div class="abs contact-row" style="left:43px;top:472px;font-size:9.6px">
      <svg width="16" height="16" viewBox="0 0 16 16"><circle cx="8" cy="8" r="8" fill="#fff"/><circle cx="8" cy="8" r="4.8" fill="none" stroke="#111" stroke-width="1"/><ellipse cx="8" cy="8" rx="2" ry="4.8" fill="none" stroke="#111" stroke-width="1"/><path d="M3.2 8h9.6" stroke="#111" stroke-width="1"/></svg>
      www.HARBORPEO-EXAMPLE.com
    </div>
  </div>

  <div class="panel panel--c cover">
    <div class="abs cover__card"></div>
    <div class="abs brand cover__name">HARBOR</div>
    <div class="abs cover__sub">EMPLOYEE MANAGEMENT, INC</div>
    <div class="abs cover__photo" role="img" aria-label="Photo of a group of smiling business professionals in suits"></div>
    <h1 class="abs cover__head" style="top:350px">PAYROLL ADMINISTRATION</h1>
    <h1 class="abs cover__head" style="top:374px">WORKERS' COMPENSATION</h1>
    <h1 class="abs cover__head" style="top:399px">UNEMPLOYMENT CLAIM<br>MANAGEMENT</h1>
    <p class="abs cover__note">We take care of the employee Administration so,<br>you can Focus on running your business.</p>
    <div class="abs call">
      <span class="call__lead">Call us</span>
      <span class="call__icon"><svg width="12" height="12" viewBox="0 0 16 16"><path d="M3 2.5l3-.7 1.5 3.6-1.7 1.3c.8 2 2.4 3.6 4.4 4.4l1.3-1.7 3.6 1.5-.7 3C8.6 14.4 1.6 7.4 3 2.5z" fill="#111"/></svg></span>
      <span class="call__num">800-555-0142</span>
    </div>
  </div>
</section>

<!-- Inside spread -->
<section class="sheet sheet--inside">

  <div class="panel panel--a intro">
    <h2 class="abs intro__title">BY SELECTING HARBOR PEO</h2>
    <p class="abs intro__text" style="top:36px">You establish a co-employer Relationship. Harbor takes on the administrative responsibility of managing your employees.</p>
    <p class="abs intro__text" style="top:70px">Our all-inclusive program includes The preparation and filing of Payroll taxes, benefit administration, workers' compensation and federal and state unemployment.</p>
    <p class="abs intro__text" style="top:104px">We work with you to ensure employee Related governmental compliance.</p>
    <svg class="abs" style="left:0;top:128px" width="216" height="381" viewBox="0 0 216 381" role="img" aria-label="Photo of many hands stacked together in teamwork">
      <defs>
        <linearGradient id="handsTone" x1="0" y1="0" x2="1" y2="1">
          <stop offset="0" stop-color="#b5603a"/>
          <stop offset=".5" stop-color="#d9946b"/>
          <stop offset="1" stop-color="#8c4a2c"/>
        </linearGradient>
      </defs>
      <path d="M0 0 C60 45 150 45 216 20 V381 H0 Z" fill="var(--gold)"/>
      <path d="M0 22 C60 70 150 62 216 40 V381 H0 Z" fill="url(#handsTone)"/>
    </svg>
  </div>

  <div class="panel panel--b">
    <h2 class="abs care__title">You focus on running your business and we take care of:</h2>
    <div class="abs care__rule"></div>
    <ul class="abs care__list">
      <li>Paycheck Calculations</li>
      <li>Record keeping</li>
      <li>Weekly, Monthly, Quarterly Tax Deposits</li>
      <li>Quarterly Tax Reporting</li>
      <li>New Hire Reporting</li>
      <li>INS Compliance</li>
      <li>IRS Compliance</li>
      <li>DOL Compliance</li>
      <li>W2 and W3</li>
      <li>Child Supports and Garnishment Administration</li>
      <li>Banking and Direct Deposits</li>
      <li>Wage Verifications</li>
      <li>Unemployment Claims</li>
      <li>Workers' Compensation Audits</li>
    </ul>
    <div class="abs brand" style="left:0;top:318px;width:218px;text-align:center;color:#fff;font-size:30px">HARBOR</div>
    <div class="abs consult">
      <div class="consult__gold">CALL FOR A<br><span style="font-size:11.4px">FREE CONSULTATION</span></div>
      <div class="consult__dark">800-555-0142</div>
      <div class="consult__or">OR</div>
      <div class="consult__gold" style="font-size:11.4px">VISIT OUR WEBSITE AT</div>
      <div class="consult__dark" style="font-size:9.4px">www.HARBORPEO-EXAMPLE.com</div>
    </div>
  </div>

  <div class="panel panel--c closing">
    <svg class="abs" style="left:0;top:0" width="224" height="200" viewBox="0 0 224 200">
      <defs>
        <linearGradient id="officeTone" x1="0" y1="0" x2="1" y2="1">
          <stop offset="0" stop-color="#e9ecef"/>
          <stop offset=".55" stop-color="#b9bcc2"/>
          <stop offset="1" stop-color="#6d6f78"/>
        </linearGradient>
      </defs>
      <rect width="224" height="200" fill="#fff"/>
      <path d="M0 0 H224 V150 C150 140 60 145 0 168 Z" fill="url(#officeTone)" role="img" aria-label="Photo of colleagues working together at a computer in an office"/>
      <path d="M0 168 C60 145 150 140 224 150 V172 C160 152 70 158 0 186 Z" fill="var(--gold)"/>
    </svg>
    <p class="abs closing__text">Let Harbor help you succeed By reducing employer overhead (insurance and taxes) while Simplifying employee administration, Ensuring governmental compliance, And increasing employee benefits.</p>
    <div class="abs closing__phone">800-555-0142</div>
    <div class="abs closing__web">www.HARBORPEO-EXAMPLE.com</div>
    <div class="abs" style="left:0;top:285px;width:224px;height:224px;background:linear-gradient(180deg,#f2f2f2 0%,#8a7a6e 45%,#2c2c30 100%)" role="img" aria-label="Photo of three smiling business professionals"></div>
  </div>
</section>

</body>
</html>
```